Geschäftspapiere für Praxis für Integrative Physiotherapie
Zielgruppe
Praxis für Integrative Physiotherapie
Aufgabenstellung
Edel und übersichtlich, gern mit Farbe. Eventuell ein Wasserzeichen.
Logo gern in Relieflack oder als Metallic-Effekt gedruckt. Das neue Logo wurde bereits erstellt und befindet sich im Anhang! Im Anhang auch ein Bild von den aktuellen Visitenkarten!

```html
<!DOCTYPE html>
<html lang="de">
<head>
<meta charset="utf-8">
<title>Briefbogen – Zentrum Wiesengrund</title>
<link href="https://fonts.googleapis.com/css2?family=Josefin+Sans:wght@300;400;600;700&display=swap" rel="stylesheet">
<style>
  :root {
    --orange: #f5ac5e;
    --orange-text: #f0a35a;
    --orange-faint: #f8d9bc;
    --ink: #1c1c1c;
    --mark: #7a7a7a;
    --page: #ffffff;
  }
  * { margin: 0; padding: 0; box-sizing: border-box; }
  html, body { width: 1200px; height: 1200px; overflow: hidden; background: var(--page); }
  body { position: relative; font-family: "Josefin Sans", sans-serif; color: var(--ink); }

  .sheet {
    position: absolute; left: 247px; top: 144px; width: 632px; height: 891px;
    background: var(--page);
    box-shadow: 2px 2px 4px rgba(0,0,0,.35);
    overflow: hidden;
  }
  .sheet-bands { position: absolute; inset: 0; width: 632px; height: 891px; }

  .brand-ring { position: absolute; left: 494px; top: 0; width: 138px; height: 138px; }

  .brand-name {
    position: absolute; right: 60px; top: 72px;
    font-size: 27px; font-weight: 600; color: var(--orange-text); letter-spacing: .2px;
  }
  .brand-claim {
    position: absolute; right: 60px; top: 115px;
    font-size: 12.5px; font-weight: 400; letter-spacing: .3px;
  }

  .sender-line { position: absolute; left: 75px; top: 145px; font-size: 7.6px; font-weight: 400; }

  .practitioner { position: absolute; right: 60px; top: 141px; text-align: right; font-size: 11.5px; font-weight: 300; line-height: 14.3px; }
  .practitioner-name { font-weight: 600; font-size: 12px; margin-bottom: 1px; }

  .fold-mark { position: absolute; left: 0; width: 11px; height: 1px; background: var(--mark); }
  .fold-mark.punch { height: 3px; }

  .footer-col { position: absolute; top: 819px; font-size: 6px; font-weight: 600; line-height: 9.1px; }
  .footer-title { color: var(--orange-text); font-size: 7.5px; font-weight: 400; letter-spacing: .3px; line-height: 10px; }
  .contact { left: 76px; }
  .bank { left: 244px; }
  .hours { left: 412px; }
  .contact-row { position: relative; }
  .contact-icon { position: absolute; left: -13px; top: 1px; width: 7px; height: 7px; }
  .hours-row { display: flex; }
  .hours-day { width: 46px; }
</style>
</head>
<body>
  <div class="sheet">
    <svg class="sheet-bands" viewBox="0 0 632 891" aria-hidden="true">
      <path d="M0 0 H252 C140 16 50 44 0 86 Z" fill="var(--orange)"/>
      <path d="M632 806 C560 856 470 882 377 891 H632 Z" fill="var(--orange)"/>
    </svg>

    <svg class="brand-ring" viewBox="0 0 138 138" aria-hidden="true">
      <circle cx="69" cy="69" r="66" fill="none" stroke="var(--orange-faint)" stroke-width="3"/>
    </svg>

    <div class="brand-name">Zentrum Wiesengrund</div>
    <div class="brand-claim">Praxis für integrative Physiotherapie</div>

    <div class="sender-line">Zentrum Wiesengrund | Lindenweg 12 | 16321 Wiesengrund</div>

    <div class="practitioner">
      <div class="practitioner-name">Tobias Wernke</div>
      <div>Physiotherapeut</div>
      <div>Masseur u. med. Bademeister</div>
      <div>Yogalehrer</div>
    </div>

    <div class="fold-mark" style="top:322px"></div>
    <div class="fold-mark punch" style="top:450px"></div>
    <div class="fold-mark" style="top:633px"></div>

    <div class="footer-col contact">
      <div class="footer-title">KONTAKT</div>
      <div class="contact-row">
        <svg class="contact-icon" viewBox="0 0 10 10"><path d="M5 10 C2 6 1.5 5 1.5 3.6 A3.5 3.5 0 0 1 8.5 3.6 C8.5 5 8 6 5 10Z" fill="var(--orange)"/><circle cx="5" cy="3.6" r="1.3" fill="#fff"/></svg>
        Lindenweg 12 | 16321 Wiesengrund</div>
      <div class="contact-row">
        <svg class="contact-icon" viewBox="0 0 10 10"><path d="M2 1 L4 1 L4.6 3.4 L3.4 4.4 C4 5.8 4.6 6.4 5.8 6.8 L6.8 5.6 L9 6.2 L9 8.2 C5 9 1 5 2 1Z" fill="var(--orange)"/></svg>
        033421 58204</div>
      <div class="contact-row">
        <svg class="contact-icon" viewBox="0 0 10 10"><rect x="2.5" y="1" width="5" height="3" fill="var(--orange)"/><rect x="1" y="4" width="8" height="3.5" rx="1" fill="var(--orange)"/><rect x="2.5" y="6.5" width="5" height="2.5" fill="var(--orange)"/></svg>
        033421 580299</div>
      <div class="contact-row">
        <svg class="contact-icon" viewBox="0 0 10 10"><rect x="1" y="2" width="8" height="6" fill="none" stroke="var(--orange)"/><path d="M1 2 L5 5.5 L9 2" fill="none" stroke="var(--orange)"/></svg>
        physio@zentrum-wiesengrund.de</div>
      <div class="contact-row">
        <svg class="contact-icon" viewBox="0 0 10 10"><path d="M9.5 0.5 L0.5 4 L4.5 5.5 L6 9.5 Z" fill="var(--orange)"/></svg>
        www.zentrum-wiesengrund.de</div>
    </div>

    <div class="footer-col bank">
      <div class="footer-title">KREDITINSTITUT</div>
      <div>Kreissparkasse Nordland</div>
      <div>IBAN: DE12 3456 7890 0012 3456 78</div>
      <div>BIC: NORDDEK1XXX</div>
      <div>St-Nr.: 071 318 55207</div>
      <div>IK - Nr.: 450318772</div>
    </div>

    <div class="footer-col hours">
      <div class="footer-title">THERAPIEZEITEN</div>
      <div class="hours-row"><span class="hours-day">Montags</span><span>8:00 - 18:30</span></div>
      <div class="hours-row"><span class="hours-day">Dienstags</span><span>8:00 - 18:00</span></div>
      <div class="hours-row"><span class="hours-day">Mittwochs</span><span>8:00 - 18:30</span></div>
      <div class="hours-row"><span class="hours-day">Donnerstags</span><span>8:00 - 18:00</span></div>
      <div class="hours-row"><span class="hours-day">Freitags</span><span>8:00 - 13:00</span></div>
    </div>
  </div>
</body>
</html>
```